Maplecrest Learning Center Posters Showing Building Blocks

We need poster designs for a School in Arizona for kids with Autism. There will be 4 such posters needed which highlight our schools building blocks. Requirements for all 4 posters are as followed: 1) We need the Maplecrest Learning Center Logo on each poster. I have included attachment. 2) The posters need the following titles: Building Block #1 (for the first poster), Building Block #2 for the 2nd poster, Building Block #3 for the 3rd poster, and Building Block #4 for the forth poster. 3) The main text and focus of the posters will be the following key words: For the first poster the words "Kids first in every decision". The words for the second poster are: "Students are friends with each other, and welcome new students with open arms." The words for the 3rd poster are: "The school is quiet, and students are working hard to do their best." The words for the 4th poster are: "Parents see amazing improvement in their child." 4) We would love to use some of the kids art from our schools if possible. Use your expertise to decide. I will send these out as well. 5) Try and design the posters around the key words from each poster 6) I am sure if landscape or portrait would be best so I will let the experts decide. All 4 posters need to be the same layout once decided.

Target Market(s)

These posters are for the school only. Prospective students/parents will see these posters so they will be used for Marketing from that perspective. We may put out into local community in future.

Industry/Entity Type

School

Font styles to use
Serif

Requirements
Must have
• 1) Logo (Maplecrest Learning Center for Growth and Discovery)
• 2) Title: as described in write up
• 3) Key words: as described in write up
Nice to have
• Kids art from school. Note: This is the first time that I have been on this site so I may have made a mistake by putting 4 posters on one project. I am assuming that I would need to pay more to have 4 posters so let me know if I need to modify the project in any way?

```html
<!DOCTYPE html>
<html lang="en">
<head>
<meta charset="utf-8">
<title>Maplecrest Learning Center – Building Block #2</title>
<link rel="stylesheet" href="https://fonts.googleapis.com/css2?family=Permanent+Marker&family=Tinos:wght@400;700&display=swap">
<style>
  :root {
    --page-bg: #e6e5e2;
    --wood-dark: #2e2824;
    --wood-mid: #4a413a;
    --wood-light: #5d544c;
    --paper-white: #ffffff;
    --quote-white: #f4f2ee;
    --brand-red: #d11f25;
    --brand-ink: #1c1c1c;
    --tape: rgba(238, 232, 212, 0.88);
    --art-tone-a: #b9a8ae;
    --art-tone-b: #c8b497;
  }
  * { margin: 0; padding: 0; box-sizing: border-box; }
  html, body {
    width: 1200px;
    height: 1148px;
    overflow: hidden;
    background: var(--page-bg);
  }
  .poster {
    position: absolute;
    left: 220px;
    top: 34px;
    width: 760px;
    height: 1080px;
    background:
      repeating-linear-gradient(180deg, rgba(255,255,255,0.03) 0 3px, rgba(0,0,0,0.06) 3px 7px),
      linear-gradient(180deg, var(--wood-mid), var(--wood-dark) 45%, var(--wood-light) 70%, var(--wood-dark));
    overflow: hidden;
  }
  .kids-art {
    position: absolute;
    left: 60px;
    top: 84px;
    width: 600px;
    height: 440px;
  }
  .kids-art svg { width: 100%; height: 100%; display: block; }
  .tape {
    position: absolute;
    width: 130px;
    height: 40px;
    background: var(--tape);
  }
  .tape--left { left: 38px; top: 94px; transform: rotate(-42deg); }
  .tape--right { left: 545px; top: 70px; transform: rotate(20deg); }
  .quote {
    position: absolute;
    left: 250px;
    top: 565px;
    font-family: "Permanent Marker", cursive;
    font-size: 28px;
    line-height: 44px;
    color: var(--quote-white);
    text-transform: uppercase;
    white-space: nowrap;
    transform: rotate(-3deg);
    transform-origin: left top;
  }
  .brand-band {
    position: absolute;
    left: 0;
    top: 832px;
    width: 100%;
    height: 216px;
    background: var(--paper-white);
  }
  .block-title {
    position: absolute;
    right: 88px;
    top: 20px;
    font-family: "Tinos", serif;
    font-weight: 700;
    font-size: 14px;
    color: var(--brand-red);
    letter-spacing: 0.3px;
  }
  .brand {
    position: absolute;
    left: 150px;
    top: 58px;
    display: flex;
    align-items: center;
    gap: 16px;
  }
  .brand-mark {
    width: 48px;
    height: 48px;
    background: var(--brand-red);
    flex: none;
  }
  .brand-name {
    font-family: "Tinos", serif;
    font-weight: 700;
    font-size: 27px;
    line-height: 32px;
    color: var(--brand-ink);
  }
</style>
</head>
<body>
  <main class="poster">
    <div class="kids-art">
      <svg viewBox="0 0 600 440" role="img" aria-label="Student artwork on torn paper, taped to the board">
        <defs>
          <linearGradient id="art-fill" x1="0" y1="0" x2="1" y2="1">
            <stop offset="0" stop-color="var(--art-tone-a)"/>
            <stop offset="1" stop-color="var(--art-tone-b)"/>
          </linearGradient>
        </defs>
        <polygon fill="url(#art-fill)" points="0,20 590,10 600,300 540,330 470,345 380,370 300,395 200,410 100,420 0,425"/>
      </svg>
    </div>
    <div class="tape tape--left"></div>
    <div class="tape tape--right"></div>

    <p class="quote">"Students are friends<br>with each other, and<br>welcome new students<br>with open arms."</p>

    <section class="brand-band">
      <h1 class="block-title">BUILDING BLOCK #2</h1>
      <div class="brand">
        <span class="brand-mark"></span>
        <p class="brand-name">Maplecrest Learning Center<br>for Growth and Discovery</p>
      </div>
    </section>
  </main>
</body>
</html>
```